Restaurant Business Card Template

I need a business card created in the same color scheme and style as the attached label. Preferably it'd be in a .ai format.

Industry/Entity Type

German Restaurant

Contact Information for Business Card

Dorine Pekko, Front of House Manager, 612.307.4419, dorine@brunhofstuberestaurant.example, info@brunhofstuberestaurant.example, 417 Tamble Ave., Lower Level, Halvorne, OR 98751.

Requirements
Must have
• Matching fonts and colors.
Nice to have
• If not able to match secondary font, something similar.

```html
<!DOCTYPE html>
<html lang="en">
<head>
<meta charset="utf-8">
<title>Brunhof Stube Restaurant – Business Card</title>
<link href="https://fonts.googleapis.com/css2?family=UnifrakturMaguntia&family=Oswald:wght@300&family=Jost:wght@400&display=swap" rel="stylesheet">
<style>
  :root {
    --page: #ece7df;
    --card-blue: #1f87d1;
    --diamond-light: #a9d3f2;
    --diamond-mid: #5fb0e6;
    --paper: #ffffff;
    --gold: #f2bd1a;
    --frame-gold: #a8842c;
    --ink: #111111;
    --white: #ffffff;
  }
  * { box-sizing: border-box; margin: 0; padding: 0; }
  html, body { width: 1200px; height: 795px; overflow: hidden; background: var(--page); }
  .card {
    position: absolute; left: 100px; top: 112px; width: 1000px; height: 571px;
    background: var(--card-blue); overflow: hidden;
    box-shadow: 0 6px 18px rgba(0,0,0,0.18);
  }
  .pattern-field {
    position: absolute; left: 0; top: 0; width: 640px; height: 571px;
    background: linear-gradient(135deg, var(--paper) 0%, var(--diamond-light) 45%, var(--paper) 70%, var(--diamond-mid) 100%);
    clip-path: polygon(0 0, 590px 0, 610px 120px, 640px 300px, 615px 571px, 0 571px);
  }
  .frame {
    position: absolute; left: 22px; top: 36px; width: 568px; height: 498px;
    border: 2px solid var(--frame-gold);
  }
  .brand {
    position: absolute; left: 170px; top: 130px; width: 330px; height: 310px;
    display: flex; flex-direction: column; align-items: center; justify-content: center; gap: 16px;
    text-align: center;
  }
  .brand-mark { width: 60px; height: 60px; border-radius: 50%; background: var(--gold); }
  .brand-name {
    font-family: "UnifrakturMaguntia", serif; color: var(--ink);
    font-size: 46px; line-height: 1.1;
  }
  .tagline {
    position: absolute; left: 34px; top: 215px; width: 120px;
    font-family: "UnifrakturMaguntia", serif; color: var(--frame-gold);
    font-size: 24px; line-height: 1.25; text-align: center;
  }
  .established {
    position: absolute; left: 510px; top: 380px;
    font-family: "UnifrakturMaguntia", serif; color: var(--frame-gold);
    font-size: 24px; line-height: 1; text-align: center;
  }
  .contact {
    position: absolute; left: 655px; top: 70px; width: 330px; color: var(--white);
    font-family: "Jost", sans-serif;
  }
  .person-name { font-family: "UnifrakturMaguntia", serif; color: var(--ink); font-size: 42px; font-weight: 400; }
  .person-title { font-family: "Oswald", sans-serif; font-weight: 300; color: var(--gold); font-size: 23px; margin-top: 2px; }
  .phone-label { font-size: 15px; margin-top: 44px; padding-left: 40px; }
  .phone { font-size: 18px; letter-spacing: 3px; margin-top: 4px; padding-left: 10px; }
  .emails { font-size: 15px; margin-top: 24px; line-height: 1.45; }
  .address { font-size: 18px; margin-top: 22px; line-height: 1.4; padding-left: 10px; }
</style>
</head>
<body>
  <div class="card">
    <div class="pattern-field" role="img" aria-label="Blue and white Bavarian diamond pattern"></div>
    <div class="frame"></div>
    <div class="tagline">Where Taste Meets Tradition</div>
    <div class="brand">
      <span class="brand-mark"></span>
      <div class="brand-name">Brunhof Stube<br>Restaurant</div>
    </div>
    <div class="established">Est.<br>1989</div>
    <div class="contact">
      <h1 class="person-name">Dorine Pekko</h1>
      <p class="person-title">Front of House Manager</p>
      <p class="phone-label">Phone/Fax</p>
      <p class="phone">(612).307.4419</p>
      <p class="emails">dorine@brunhofstuberestaurant.example<br>info@brunhofstuberestaurant.example</p>
      <p class="address">417 Tamble Ave., Lower Level,<br>Halvorne, OR 98751</p>
    </div>
  </div>
</body>
</html>
```